Editorial Website Design for High-End Custom Millwork Firm

Design (no development) for a 5-7 page website for a high-end custom architectural millwork firm. Editorial, magazine-quality aesthetic — think Dwelling Quarterly and top-tier millwork studios (Owen Tallard, Vorko). Full brief, reference sites, and project photography attached. We have uploaded a sample of our photography to use in your design. PLEASE READ PDF DOCUMENT BRIEF!!!

```html
<!DOCTYPE html>
<html lang="en">
<head>
<meta charset="utf-8">
<title>Ashgrove Millwork — The Mercantile Exchange</title>
<link href="https://fonts.googleapis.com/css2?family=Newsreader:ital,opsz,wght@0,6..72,400;1,6..72,400&family=Inter:wght@400;500;600&display=swap" rel="stylesheet">
<style>
:root{
  --ink:#1c1b1a;
  --black:#000;
  --nav:#252322;
  --paper:#f8f6f3;
  --white:#fff;
  --muted:#555250;
  --label:#3a3836;
  --rule:#bdb8b2;
  --accent:#5a4a40;
  --footer-text:#8d8a86;
  --serif:'Newsreader',Georgia,serif;
  --sans:'Inter',Helvetica,Arial,sans-serif;
}
*{margin:0;padding:0;box-sizing:border-box}
html,body{width:1200px;height:4348px;overflow:hidden;background:var(--black)}
body{position:relative;font-family:var(--sans);color:var(--ink)}
.abs{position:absolute}
.eyebrow{font-family:var(--sans);font-size:8.5px;font-weight:600;letter-spacing:.14em;text-transform:uppercase}

/* nav */
.site-nav{left:59px;top:81px;width:1082px;height:67px;background:var(--nav)}
.logo{font-family:var(--serif);font-size:26px;color:var(--white);letter-spacing:-.01em}
.site-nav .logo{left:61px;top:17px}
.nav-links{left:353px;top:25px;display:flex;gap:30px;list-style:none}
.nav-links li{font-size:8.5px;letter-spacing:.12em;color:#a9a5a0;font-weight:500}
.nav-links li.active{color:var(--white);border-bottom:1px solid var(--white);padding-bottom:3px}
.inquire{left:942px;top:19px;width:79px;height:28px;background:var(--accent);color:var(--white);font-size:8.5px;font-weight:600;letter-spacing:.12em;display:flex;align-items:center;justify-content:center}

/* hero */
.hero{left:59px;top:148px;width:1082px;height:600px;background:linear-gradient(160deg,#4a3e33 0%,#7a6650 35%,#5d5a55 60%,#2f2c29 100%)}
.hero .eyebrow{left:61px;top:260px;color:var(--white)}
.hero-title{left:61px;top:280px;width:720px;font-family:var(--serif);font-size:68px;line-height:70px;font-weight:400;color:var(--white);letter-spacing:-.01em}

/* specification */
.spec{left:59px;top:748px;width:1082px;height:977px;background:var(--paper)}
.spec-rule{left:61px;top:96px;width:309px;height:1px;background:var(--muted)}
.spec-list{left:61px;top:123px}
.spec-list .eyebrow{font-size:8px;color:var(--ink);margin-bottom:28px;display:block}
.spec-list dt{font-size:7.5px;font-weight:600;letter-spacing:.14em;color:var(--label);margin-bottom:6px}
.spec-list dd{font-size:13px;line-height:22px;color:var(--ink);margin-bottom:13px}
.pull{left:515px;top:112px;font-family:var(--serif);font-style:italic;font-size:27px;line-height:31px;color:var(--ink)}
.spec-body{left:515px;top:200px;width:480px;font-size:12.8px;line-height:22px;color:var(--muted)}
.spec-photo{left:61px;top:410px;width:960px;height:471px;background:linear-gradient(90deg,#efebe5 0%,#e6dccd 40%,#b79b78 55%,#ede8e0 80%,#e3ddd3 100%)}
.next-btn{left:927px;top:386px;width:73px;height:71px;background:rgba(80,76,72,.45)}

/* material */
.material{left:59px;top:1725px;width:1082px;height:694px;background:var(--white)}
.material h2{left:61px;top:226px;font-family:var(--serif);font-size:26px;line-height:31px;font-weight:400}
.material p{left:61px;top:313px;width:345px;font-size:11.5px;line-height:19.7px;color:var(--muted)}
.text-link{left:61px;top:450px;font-size:8.5px;font-weight:600;letter-spacing:.1em;border-bottom:1px solid var(--ink);padding-bottom:3px;color:var(--ink)}
.material-photo{left:550px;top:91px;width:471px;height:513px;background:linear-gradient(180deg,#d9d6cf 0%,#6e4a33 30%,#8a5c3e 60%,#a9a59c 100%)}

/* detail */
.detail{left:59px;top:2419px;width:1082px;height:834px;background:var(--paper)}
.detail .eyebrow{left:0;width:1082px;top:96px;text-align:center;font-size:8px;color:var(--muted)}
.detail h2{left:0;width:1082px;top:117px;text-align:center;font-family:var(--serif);font-size:38px;font-weight:400}
.detail-card{top:211px;width:456px}
.detail-photo{height:397px}
.card-a .detail-photo{background:linear-gradient(180deg,#6a3f22 0%,#c9c3b8 40%,#9c5a2a 65%,#7a421e 100%)}
.card-b .detail-photo{background:linear-gradient(90deg,#7a8560 0%,#c9cbc0 35%,#efece6 60%,#d8d2c4 100%)}
.detail-card h3{margin-top:20px;font-size:8px;font-weight:600;letter-spacing:.12em}
.detail-card p{margin-top:9px;width:340px;font-size:11px;line-height:19px;color:var(--muted)}

/* testimonial */
.testimonial{left:59px;top:3253px;width:1082px;height:434px;background:var(--black);text-align:center}
.quote-mark{left:0;width:1082px;top:86px;font-size:13px;font-weight:600;color:#6b6864}
.testimonial blockquote{left:141px;width:800px;top:125px;font-family:var(--serif);font-style:italic;font-size:41px;line-height:42px;color:var(--white)}
.testimonial cite{left:0;width:1082px;top:331px;font-style:normal;font-size:8.5px;font-weight:600;letter-spacing:.12em;color:#cfcbc6}

/* next project */
.next-project{left:59px;top:3687px;width:1082px;height:241px;background:var(--paper)}
.next-rule{left:0;top:87px;width:1082px;height:1px;background:#e8e4df}
.next-project .eyebrow{left:61px;top:94px;font-size:8px;color:var(--muted)}
.next-project h2{left:61px;top:112px;font-family:var(--serif);font-size:40px;font-weight:400}
.next-arrow{left:987px;top:122px}

/* footer */
.site-footer{left:59px;top:3928px;width:1082px;height:420px}
.site-footer .logo{left:61px;top:90px}
.tagline{left:61px;top:147px;width:160px;font-size:11px;line-height:19px;color:var(--footer-text)}
.footer-col{top:92px}
.footer-col h4{font-size:8px;font-weight:600;letter-spacing:.12em;color:var(--white);margin-bottom:16px}
.footer-col li{list-style:none;font-size:11.5px;line-height:25.5px;color:var(--footer-text)}
.copyright{margin-top:26px;font-size:8px;line-height:12px;letter-spacing:.06em;color:#6c6965;width:190px}
.legal{left:61px;top:269px;display:flex;gap:24px;font-size:8px;letter-spacing:.08em;color:#6c6965}
</style>
</head>
<body>

<header class="site-nav abs">
  <div class="logo abs">Ashgrove Millwork</div>
  <ul class="nav-links abs">
    <li class="active">PROJECTS</li><li>INDIVIDUAL</li><li>SERVICES</li><li>ABOUT</li><li>BLOG</li><li>CONTACT</li>
  </ul>
  <div class="inquire abs">INQUIRE</div>
</header>

<section class="hero abs" role="img" aria-label="Retail interior with arched walnut shelving, a curved display table and merchandise under warm light">
  <div class="eyebrow abs">Featured Case Study</div>
  <h1 class="hero-title abs">The Mercantile Exchange: An Exercise in Walnut and Light</h1>
</section>

<section class="spec abs">
  <div class="spec-rule abs"></div>
  <div class="spec-list abs">
    <span class="eyebrow">The Specification</span>
    <dl>
      <dt>LOCATION</dt><dd>Charleston, South Carolina</dd>
      <dt>MATERIALS</dt><dd>Rift Sawn Black Walnut, Calacatta<br>Borghini Marble, Burnished Brass</dd>
      <dt>ARCHITECT</dt><dd>Larkin &amp; Vale Associates</dd>
    </dl>
  </div>
  <p class="pull abs">"A dialogue between tradition and<br>modernity."</p>
  <p class="spec-body abs">The Mercantile Exchange required a seamless integration of high-performance retail utility with the warmth of bespoke residential cabinetry. Our challenge was to execute 4,000 linear feet of walnut shelving and cabinetry with a tolerance of less than 1/32nd of an inch, ensuring that every grain matched perfectly across twenty-foot spans.</p>
  <div class="spec-photo abs" role="img" aria-label="Bright kitchen with white oak island, cream cabinetry and brass pendant lights">
    <div class="next-btn abs">
      <svg width="73" height="71" viewBox="0 0 73 71"><path d="M14 36H58M44 22L58 36L44 50" fill="none" stroke="#fff" stroke-width="1.5"/></svg>
    </div>
  </div>
</section>

<section class="material abs">
  <h2 class="abs">Material Sourcing &amp;<br>Selection</h2>
  <p class="abs">Every plank of American Black Walnut was hand-selected from a single sustainable source in the Appalachian valley. This commitment to origin allowed us to maintain consistent coloration and figure throughout the entire project, creating a sense of monolithic calm that is rarely achieved at this scale.</p>
  <div class="text-link abs">OUR SUSTAINABILITY STANDARDS</div>
  <div class="material-photo abs" role="img" aria-label="Walnut reception desk with a perforated screen wall, stone counters and brass pendants"></div>
</section>

<section class="detail abs">
  <div class="eyebrow abs">Craft in Focus</div>
  <h2 class="abs">Defining the Detail</h2>
  <article class="detail-card card-a abs" style="left:61px">
    <div class="detail-photo" role="img" aria-label="Figured walnut cabinetry with lit glass-front upper cabinets"></div>
    <h3>TECHNICAL PRECISION</h3>
    <p>The integration of hidden LED drivers within the structural millwork required a complex internal routing system that remains entirely invisible to the guest.</p>
  </article>
  <article class="detail-card card-b abs" style="left:565px">
    <div class="detail-photo" role="img" aria-label="Painted bar cabinetry with brass hardware and patterned wallcovering"></div>
    <h3>INTEGRATED HARDWARE</h3>
    <p>Custom brass hardware was recessed flush into the walnut faces, requiring CNC precision combined with hand-tool refinement.</p>
  </article>
</section>

<section class="testimonial abs">
  <div class="quote-mark abs">99</div>
  <blockquote class="abs">Ashgrove Millwork didn't just build our design; they interrogated every joint and finish until the physical reality exceeded our digital intent.</blockquote>
  <cite class="abs">— JULIAN VALE, PRINCIPAL ARCHITECT</cite>
</section>

<section class="next-project abs">
  <div class="next-rule abs"></div>
  <div class="eyebrow abs">View Next Project</div>
  <h2 class="abs">The Riverside Residency</h2>
  <svg class="next-arrow abs" width="20" height="20" viewBox="0 0 20 20"><path d="M2 10H17M11 4L17 10L11 16" fill="none" stroke="#1c1b1a" stroke-width="1.5"/></svg>
</section>

<footer class="site-footer abs">
  <div class="logo abs">Ashgrove Millwork</div>
  <p class="tagline abs">Mastering the intersection of architecture and timber since 1994.</p>
  <div class="footer-col abs" style="left:306px">
    <h4>GLOBAL OFFICES</h4>
    <ul><li>New York</li><li>Charleston</li><li>London</li></ul>
  </div>
  <div class="footer-col abs" style="left:550px">
    <h4>CONNECT</h4>
    <ul><li>Photo Journal</li><li>Professional</li><li>Film Reel</li></ul>
  </div>
  <div class="footer-col abs" style="left:795px">
    <h4>INQUIRIES</h4>
    <ul><li>hello@ashgrovemillwork.com</li></ul>
    <p class="copyright">© 2024 Ashgrove Millwork. All Rights Reserved.</p>
  </div>
  <div class="legal abs">
    <span>Woodwork Quality Council Certified</span>
    <span>Minority Business Enterprise (MBE)</span>
    <span>Privacy Policy</span>
    <span>Terms of Service</span>
  </div>
</footer>

</body>
</html>
```